Homepage mockup for PivotScoreHub.com

I would like a homepage mockup of pivotscorehub.com.

Basically what the site does, is it allows a person to upload a video of a gymnastics routine and our certified judges will judge the routine providing a score, as well as provide a critique and feedback as to why they gave you that score. Many times people don't know why they got the score they did at a gymnastics competition, so this site aims to provide reasoning behind it.

I have started to design the homepage myself (see attached), and like it, but I'd like a professional to finish the layout, or even come up with something really wow and original. I like clean, typically simple design.

THIS IS AN OLD VERSION OF THE SITE (http://esite.kralvenot.com/) This should only be used so you can get an idea of what the site is about. I DO NOT want the new site to look like this, but the basic concept and content remains the same.

DESIGNER FILES CAN BE DOWNLOADED HERE (http://kralvenot.com/files.aspx)

Target Market(s)

Gymnastic type people, parents of gymnasts, coaches, etc.

Industry/Entity Type

It Professional

Requirements
Must have
• -Pivot score hub logo (provided)
-Not required, but I have attached the main photo I used in my mockup (AI File)
*A step by step graphic(s) depicting the process for a user. A How it works sort of explanation. Should be eye catching, not just text.

-Step 1: Videotape your gymnastic routine.
-Step 2: Create an account and share us your video.
-Step 3: Our certified judges will score and critique your routine, fully explaining the reasons behind their score.

```html
<!DOCTYPE html>
<html lang="en">
<head>
<meta charset="utf-8">
<title>Pivot score hub — Your Personal Gymnastic Judge</title>
<link rel="stylesheet" href="https://fonts.googleapis.com/css2?family=Arimo:wght@400;700&family=Kalam:wght@300;400&family=Tinos:wght@400;700&display=swap">
<style>
  :root {
    --brand-red: #9b1b1e;
    --brand-blue: #1e6fa0;
    --nav-active: #1a87c0;
    --ink: #3a3a3a;
    --body-text: #6a6a6a;
    --step-label: #7a6d66;
    --page-bg: #f3f3f3;
    --header-top: #ffffff;
    --header-bottom: #e9ecf1;
    --beam-top: #e3d4c0;
    --beam-bottom: #c9b094;
    --footer-bg: #262626;
    --footer-text: #cfcfcf;
    --cta-blue-top: #3a6fd0;
    --cta-blue-bottom: #1c3fa0;
    --member-red-top: #c0392b;
    --member-red-bottom: #8e1a12;
    --blog-orange: #f08a17;
    --social-dark: #3b3b3b;
  }
  * { margin: 0; padding: 0; box-sizing: border-box; }
  html, body { width: 1200px; height: 887px; overflow: hidden; }
  body {
    font-family: "Arimo", Arial, sans-serif;
    background: var(--page-bg);
    position: relative;
  }
  a { text-decoration: none; }
  .page {
    position: absolute; inset: 0;
    background: radial-gradient(ellipse at 45% 45%, #fbfbfb 0%, #f1f1f1 55%, #e6e6e6 100%);
  }

  /* Header */
  .site-header {
    position: absolute; left: 0; top: 0; width: 1200px; height: 121px;
    background: linear-gradient(to bottom, var(--header-top) 0%, #f9fafc 60%, var(--header-bottom) 100%);
    border-bottom: 3px solid #ffffff;
    box-shadow: 0 1px 2px rgba(0,0,0,.08);
  }
  .brand {
    position: absolute; left: 93px; top: 52px;
    display: flex; align-items: center; gap: 10px;
    font-size: 30px; font-weight: 700; color: var(--brand-blue);
    letter-spacing: -0.5px;
  }
  .brand-mark { width: 22px; height: 22px; border-radius: 50%; background: var(--brand-red); }
  .main-nav a {
    position: absolute; top: 73px; font-size: 14.5px; color: var(--brand-red);
    line-height: 18px;
  }
  .main-nav a.is-active {
    top: 67px; left: 446px; width: 66px; height: 30px; line-height: 30px;
    text-align: center; color: #fff; border-radius: 3px;
    background: linear-gradient(to bottom, #2b9ad2, var(--nav-active));
  }

  .member-login {
    position: absolute; left: 938px; top: 122px; width: 171px; height: 44px;
    background: linear-gradient(to bottom, #ffffff, #eeeeee);
    border-radius: 0 0 14px 14px;
    box-shadow: 0 2px 3px rgba(0,0,0,.15);
    display: flex; align-items: center; gap: 10px; padding-left: 22px;
    font-size: 14.5px; color: #666;
  }

  /* Hero */
  .score-cards .card {
    position: absolute; background: #fff; width: 64px; height: 96px;
    box-shadow: 1px 2px 4px rgba(0,0,0,.25);
    font-family: "Tinos", Georgia, serif; font-weight: 400;
    font-size: 46px; color: #444; display: flex; align-items: center; justify-content: center;
  }
  .headline {
    position: absolute; left: 240px; top: 197px; font-weight: 300;
    font-family: "Kalam", cursive; font-size: 26px; line-height: 42px;
  }
  .headline .line-one { color: var(--brand-red); letter-spacing: 0.6px; }
  .headline .line-two { color: var(--brand-blue); letter-spacing: 0.6px; }
  .headline .why { font-family: "Arimo", Arial, sans-serif; font-weight: 400; color: var(--ink); font-size: 24px; }

  .cta-frame {
    position: absolute; left: 245px; top: 307px; width: 270px; height: 69px;
    border-radius: 22px; background: linear-gradient(to bottom, #e6e6e6, #d2d2d2);
    box-shadow: inset 0 1px 2px rgba(0,0,0,.15);
  }
  .cta-start {
    position: absolute; left: 9px; top: 9px; width: 252px; height: 50px; border-radius: 14px;
    background: linear-gradient(to bottom, var(--cta-blue-top), var(--cta-blue-bottom));
    box-shadow: 0 2px 3px rgba(0,0,0,.3);
    color: #fff; display: flex; align-items: center; padding-left: 10px;
  }
  .cta-start .small { font-size: 12.5px; font-weight: 700; line-height: 13px; text-align: right; width: 116px; }
  .cta-start .big { font-size: 20px; font-weight: 700; margin-left: 14px; letter-spacing: -0.3px; }

  .intro {
    position: absolute; left: 103px; top: 406px; width: 496px;
    font-size: 13.5px; line-height: 23px; color: var(--body-text);
  }

  .steps { position: absolute; left: 80px; top: 530px; width: 580px; height: 180px; overflow: visible; }

  /* Photo area */
  .hero-photo {
    position: absolute; left: 595px; top: 250px; width: 570px; height: 565px;
    background: radial-gradient(ellipse at 45% 45%, rgba(40,35,35,.55) 0%, rgba(150,120,110,.35) 40%, rgba(230,225,222,0) 72%);
  }

  .tagline {
    position: absolute; left: 880px; top: 570px; width: 230px; text-align: center;
    font-size: 24px; line-height: 34px; color: #8b1a1a;
  }
  .become-member {
    position: absolute; left: 896px; top: 649px; width: 205px; height: 37px;
    border-radius: 19px; background: linear-gradient(to bottom, var(--member-red-top), var(--member-red-bottom));
    box-shadow: 0 0 0 3px #e2e2e2, 0 2px 4px rgba(0,0,0,.3);
    color: #fff; font-size: 14px; font-weight: 700;
    display: flex; align-items: center; padding-left: 20px;
  }
  .become-member .arrow {
    position: absolute; right: 10px; top: 9px; width: 19px; height: 19px; border-radius: 50%;
    background: #5a1009;
  }

  /* Beam band */
  .beam {
    position: absolute; left: 0; top: 770px; width: 1200px; height: 73px;
    background: linear-gradient(to bottom, var(--beam-top) 0%, #eadfcf 20%, var(--beam-bottom) 100%);
    border-top: 2px solid #d9c8b0;
  }
  .rss-square { position: absolute; left: 89px; top: 803px; width: 16px; height: 16px; background: var(--blog-orange); border-radius: 2px; }
  .blog-link {
    position: absolute; left: 111px; top: 798px; width: 102px; height: 25px;
    background: linear-gradient(to bottom, #f7a23b, #e5730c); color: #fff;
    font-family: "Tinos", Georgia, serif; font-weight: 700; font-size: 13.5px;
    display: flex; align-items: center; justify-content: center;
  }
  .social { position: absolute; top: 798px; width: 25px; height: 25px; border-radius: 50%; background: var(--social-dark); }

  /* Footer */
  .site-footer {
    position: absolute; left: 0; top: 843px; width: 1200px; height: 44px;
    background: var(--footer-bg); color: var(--footer-text);
    font-size: 12.5px; text-align: center; line-height: 44px;
  }
</style>
</head>
<body>
<div class="page">

  <header class="site-header">
    <div class="brand"><span class="brand-mark"></span>Pivot score hub</div>
    <nav class="main-nav">
      <a class="is-active" href="#">Home</a>
      <a href="#" style="left:544px">About us</a>
      <a href="#" style="left:642px">How it works</a>
      <a href="#" style="left:764px">Sample</a>
      <a href="#" style="left:856px">Members Area</a>
      <a href="#" style="left:989px">Contact</a>
      <a href="#" style="left:1081px">FAQ</a>
    </nav>
  </header>

  <a class="member-login" href="#">
    <svg width="22" height="28" viewBox="0 0 22 28" aria-hidden="true">
      <path d="M5 12 V8 a6 6 0 0 1 12 0 V12" fill="none" stroke="#777" stroke-width="3"/>
      <rect x="2" y="12" width="18" height="15" rx="2" fill="#888"/>
      <rect x="4" y="14" width="14" height="4" fill="#aaa"/>
    </svg>
    Memeber Login
  </a>

  <div class="hero-photo" role="img" aria-label="Gymnast in a black leotard holding a split handstand on a balance beam"></div>

  <div class="score-cards">
    <div class="card" style="left:159px;top:196px">5</div>
    <div class="card" style="left:104px;top:226px">1</div>
    <div class="card" style="left:151px;top:281px">10</div>
  </div>

  <h1 class="headline">
    <div class="line-one">Judges only give you a number....</div>
    <div class="line-two">...We explain the reason <span class="why">WHY</span></div>
  </h1>

  <div class="cta-frame">
    <a class="cta-start" href="#">
      <span class="small">Upload your video<br>&amp; get critiqued!</span>
      <span class="big">Get started</span>
    </a>
  </div>

  <p class="intro">Registration is FREE and only takes a minute, donec et ligula elit, vel consectetur sem. Nunc semper congue suscipit. Mauris nibh massa, scelerisque in placerat aliquam, pretium a orci. Phasellus sit amet nulla sit amet erat placerat porta sed posuere ipsum.</p>

  <svg class="steps" viewBox="0 0 580 180" aria-label="How it works: record your routine, sign up and upload, get the why">
    <defs>
      <radialGradient id="stepFill" cx="50%" cy="35%" r="65%">
        <stop offset="0" stop-color="#ffffff"/>
        <stop offset="1" stop-color="#dcdcdc"/>
      </radialGradient>
      <path id="arc1" d="M10 124 A77 77 0 0 1 164 124"/>
      <path id="arc2" d="M209 124 A77 77 0 0 1 363 124"/>
      <path id="arc3" d="M408 124 A77 77 0 0 1 562 124"/>
    </defs>
    <g>
      <circle cx="87" cy="104" r="64" fill="#d8d8d8"/>
      <circle cx="87" cy="104" r="60" fill="url(#stepFill)"/>
      <circle cx="286" cy="104" r="64" fill="#d8d8d8"/>
      <circle cx="286" cy="104" r="60" fill="url(#stepFill)"/>
      <circle cx="485" cy="104" r="64" fill="#d8d8d8"/>
      <circle cx="485" cy="104" r="60" fill="url(#stepFill)"/>
    </g>
    <g fill="#7a6d66" font-family="Arimo, Arial, sans-serif" font-size="17" text-anchor="middle">
      <text><textPath href="#arc1" startOffset="50%">Record your Routine</textPath></text>
      <text><textPath href="#arc2" startOffset="50%">Sign up and Upload</textPath></text>
      <text><textPath href="#arc3" startOffset="50%">Get the “Why”</textPath></text>
    </g>
    <rect x="56" y="80" width="64" height="46" rx="3" fill="#cfcfcf" stroke="#999"/>
    <rect x="60" y="84" width="56" height="34" fill="#1e1e1e"/>
    <path d="M82 91 L96 101 L82 111 Z" fill="#fff"/>
    <rect x="60" y="120" width="56" height="3" fill="#555"/>
    <rect x="60" y="120" width="18" height="3" fill="#c0392b"/>
    <path d="M286 78 L306 100 L295 100 L295 124 L277 124 L277 100 L266 100 Z" fill="#4f86d6"/>
    <circle cx="485" cy="104" r="25" fill="#1da9e0"/>
    <text x="485" y="116" text-anchor="middle" fill="#fff" font-family="Arimo, Arial, sans-serif" font-weight="700" font-size="32">?</text>
    <path d="M152 112 Q175 125 198 108" fill="none" stroke="#777" stroke-width="2"/>
    <path d="M190 104 L199 107 L193 114" fill="none" stroke="#777" stroke-width="2"/>
    <path d="M351 104 Q372 92 392 102" fill="none" stroke="#777" stroke-width="2"/>
    <path d="M384 96 L393 102 L385 107" fill="none" stroke="#777" stroke-width="2"/>
  </svg>

  <div class="tagline">Your Personal<br>Gymnastic Judge!</div>
  <a class="become-member" href="#">BECOME A MEMBER<span class="arrow"></span></a>

  <div class="beam"></div>
  <span class="rss-square"></span>
  <a class="blog-link" href="#">Read our Blog</a>
  <span class="social" style="left:978px"></span>
  <span class="social" style="left:1013px"></span>
  <span class="social" style="left:1048px"></span>
  <span class="social" style="left:1083px">
    <svg width="25" height="25" viewBox="0 0 25 25" aria-label="Email">
      <rect x="6" y="8" width="13" height="9" fill="none" stroke="#fff" stroke-width="1.5"/>
      <path d="M6 8 L12.5 13.5 L19 8" fill="none" stroke="#fff" stroke-width="1.5"/>
    </svg>
  </span>

  <footer class="site-footer">Copyright ©&nbsp; 2012&nbsp; www.pivotscorehub.com&nbsp;&nbsp; All rights reserved.</footer>
</div>
</body>
</html>
```